Cover for a short novel to be published as an e-book.

I'm looking for an image to use for my e-book cover. It's a short (~42k words) novel/novella that deals humorously with the afterlife and some religious/mythological themes.

I was thinking something that was more graphic design-based rather than illustrative, and it would be awesome if it could somehow convey that it's a light, humorous story.

I plan to self-publish, so the image will end up being fairly small, but it should have some pop to draw people in.

Here's the text for the cover:

A Quiet Hour Before Supper
a novel(la) by Colin Brasby

```html
<!DOCTYPE html>
<html lang="en">
<head>
<meta charset="utf-8">
<title>A Quiet Hour Before Supper – Cover</title>
<link href="https://fonts.googleapis.com/css2?family=Marcellus&family=Marcellus+SC&family=Open+Sans:wght@600&display=swap" rel="stylesheet">
<style>
  :root {
    --stage: #e9e9ea;
    --ink: #050505;
    --gold: #f6e9b4;
    --gold-glow: rgba(255, 214, 120, 0.6);
    --rose: #f2b4d2;
    --crimson: #c24a5a;
    --body-grey: #9c9c9c;
    --box-grey: #1b1b1b;
    --box-text: #bdbdbd;
    --art-sun: #ffb347;
    --art-orange: #f26a2a;
    --art-coral: #e2413a;
    --art-magenta: #a9306a;
    --art-plum: #4a1a4e;
  }
  * { box-sizing: border-box; margin: 0; padding: 0; }
  html, body { width: 1200px; height: 800px; overflow: hidden; }
  body { background: var(--stage); font-family: "Marcellus", serif; }

  .cover-spread {
    position: absolute;
    left: 185px; top: 95px;
    width: 830px; height: 610px;
    display: flex;
    box-shadow: 0 14px 40px rgba(0,0,0,0.25);
  }

  /* Back cover */
  .back-cover {
    width: 400px; height: 100%;
    background: var(--ink);
    padding: 22px 20px 0;
    position: relative;
  }
  .back-title {
    font-weight: 400;
    color: var(--gold);
    text-align: center;
    font-size: 27px;
    line-height: 1.13;
    letter-spacing: 0.5px;
    text-shadow: 0 0 6px var(--gold-glow);
  }
  .back-author {
    font-family: "Marcellus SC", serif;
    color: var(--crimson);
    text-align: right;
    font-size: 14px;
    margin: 4px 4px 8px 0;
  }
  .blurb {
    font-family: "Open Sans", sans-serif;
    font-weight: 600;
    font-size: 9.2px;
    line-height: 14.2px;
    color: var(--body-grey);
    text-align: justify;
    text-align-last: center;
    max-height: 400px;
    overflow: hidden;
  }
  .back-boxes {
    position: absolute;
    left: 34px; right: 34px; bottom: 18px;
    display: flex;
    justify-content: space-between;
  }
  .isbn-box, .logo-box {
    width: 80px; height: 60px;
    background: var(--box-grey);
    color: var(--box-text);
    font-family: "Open Sans", sans-serif;
    font-size: 8px;
    display: flex; align-items: center; justify-content: center;
  }

  /* Spine */
  .spine {
    width: 30px; height: 100%;
    background: var(--ink);
    position: relative;
    border-left: 1px solid #1a1a1a;
    border-right: 1px solid #1a1a1a;
  }
  .spine-title, .spine-author {
    position: absolute;
    left: 50%;
    writing-mode: vertical-rl;
    transform: translateX(-50%);
    white-space: nowrap;
  }
  .spine-title {
    top: 16px;
    color: var(--gold);
    font-size: 17px;
    letter-spacing: 1px;
    text-shadow: 0 0 4px var(--gold-glow);
  }
  .spine-author {
    bottom: 24px;
    font-family: "Marcellus SC", serif;
    color: var(--body-grey);
    font-size: 7px;
  }

  /* Front cover */
  .front-cover {
    width: 400px; height: 100%;
    background: var(--ink);
    position: relative;
    display: flex; flex-direction: column;
  }
  .title-band {
    height: 122px;
    display: flex; align-items: center; justify-content: center;
  }
  .front-title {
    font-weight: 400;
    color: var(--gold);
    text-align: center;
    font-size: 34px;
    line-height: 1.12;
    letter-spacing: 0.5px;
    text-shadow: 0 0 8px var(--gold-glow), 0 0 2px var(--gold-glow);
  }
  .cover-art {
    flex: 1;
    background:
      radial-gradient(circle at 72% 22%, var(--art-sun) 0%, rgba(255,179,71,0) 45%),
      linear-gradient(180deg, var(--art-orange) 0%, var(--art-coral) 38%, var(--art-magenta) 70%, var(--art-plum) 100%);
  }
  .byline {
    position: absolute;
    left: 0; right: 0; bottom: 24px;
    text-align: center;
  }
  .byline-lead {
    display: block;
    font-size: 12px;
    letter-spacing: 1.5px;
    color: var(--gold);
    margin-bottom: 4px;
  }
  .front-author {
    display: block;
    font-family: "Marcellus SC", serif;
    color: var(--rose);
    font-size: 19px;
    letter-spacing: 1px;
  }
</style>
</head>
<body>
  <main class="cover-spread">
    <section class="back-cover">
      <h2 class="back-title">A QUIET HOUR<br>BEFORE SUPPER</h2>
      <p class="back-author">Colin Brasby</p>
      <p class="blurb">Lorem ipsum dolor sit amet, consectetur adipisicing elit, sed do eiusmod tempor incididunt ut labore et dolore magna aliqua. Ut enim ad minim veniam, quis nostrud exercitation. Lorem ipsum dolor sit amet, consectetur adipisicing elit, sed do eiusmod tempor incididunt ut labore et dolore magna aliqua. Ut enim ad minim veniam, quis nostrud exercitation. Lorem ipsum dolor sit amet, consectetur adipisicing elit, sed do eiusmod tempor incididunt ut labore et dolore magna aliqua. Ut enim ad minim veniam, quis nostrud exercitation. Lorem ipsum dolor sit amet, consectetur adipisicing elit, sed do eiusmod tempor incididunt ut labore et dolore magna aliqua. Ut enim ad minim veniam, quis nostrud exercitation. Lorem ipsum dolor sit amet, consectetur adipisicing elit, sed do eiusmod tempor incididunt ut labore et dolore magna aliqua. Ut enim ad minim veniam, quis nostrud exercitation. Lorem ipsum dolor sit amet, consectetur adipisicing elit, sed do eiusmod tempor incididunt ut labore et dolore magna aliqua. Ut enim ad minim veniam, quis nostrud exercitation. Lorem ipsum dolor sit amet, consectetur adipisicing elit, sed do eiusmod tempor incididunt ut labore et dolore magna aliqua. Ut enim ad minim veniam, quis nostrud exercitation. Lorem ipsum dolor sit amet, consectetur adipisicing elit, sed do eiusmod tempor incididunt ut labore et dolore magna aliqua. Ut enim ad minim veniam, quis nostrud exercitation. Lorem ipsum dolor sit amet, consectetur adipisicing elit, sed do eiusmod tempor incididunt ut labore et dolore magna aliqua. Ut enim ad minim veniam, quis nostrud exercitation.</p>
      <div class="back-boxes">
        <div class="isbn-box">ISBN</div>
        <div class="logo-box">LOGO</div>
      </div>
    </section>

    <section class="spine">
      <span class="spine-title">A QUIET HOUR BEFORE SUPPER</span>
      <span class="spine-author">Colin Brasby</span>
    </section>

    <section class="front-cover">
      <header class="title-band">
        <h1 class="front-title">A QUIET HOUR<br>BEFORE SUPPER</h1>
      </header>
      <div class="cover-art" role="img" aria-label="Playful painted portrait of a young man with tousled dark hair, glowing in warm orange, coral and magenta tones"></div>
      <p class="byline">
        <span class="byline-lead">a novel(la) by</span>
        <span class="front-author">Colin Brasby</span>
      </p>
    </section>
  </main>
</body>
</html>
```